Business Card Design Project

We need a business card design template for a direct sales company that is branded to the company but the name information can be changed for the representatives. The card needs to include the company logo and website...www.gokelvara.example. It should also include the Customer Service number which is 1-800-482-Kelvra.

The front should have a space with the name and a place for their phone contact information and email address.
Updates

The card should be two sided.  It could also include the tagline "Kelvra is all about K!" or any of the information from www.gokelvara.example.

I am uploading the other formats that I currently have for the logo.

Thank you

Target Market(s)

The representatives are teenage girls that are 13-19 but they are selling products to all ages.

Industry/Entity Type

Business

Requirements
Must have
• A field with the toll free customer service number.
The company logo.
The company website information.
The company representative name.
The company representative phone number.
The company representative email contact info.
Nice to have
• QR Code which we already have.
Should not have
• Do not make it look like a design for children. It should be modern and professional but sophisticated.

```html
<!DOCTYPE html>
<html lang="en">
<head>
<meta charset="utf-8">
<title>Kelvra Business Card</title>
<link href="https://fonts.googleapis.com/css2?family=Tinos:wght@400;700&display=swap" rel="stylesheet">
<style>
  :root {
    --backdrop: #5a2a26;
    --card: #e6bcb1;
    --card-edge: #d9aa9e;
    --ink: #151111;
    --brand-pink: #e0157f;
    --brand-grey: #4a4a4c;
  }
  * { box-sizing: border-box; margin: 0; padding: 0; }
  html, body {
    width: 1200px;
    height: 960px;
    overflow: hidden;
    background: var(--backdrop);
    font-family: "Tinos", "Times New Roman", serif;
    color: var(--ink);
  }
  .canvas {
    position: relative;
    width: 1200px;
    height: 960px;
  }
  .card {
    position: absolute;
    left: 270px;
    width: 660px;
    height: 320px;
    background: var(--card);
    border: 1px solid var(--card-edge);
    border-radius: 12px;
    box-shadow: 0 6px 18px rgba(0,0,0,0.35);
  }
  .card-back { top: 110px; }
  .card-front { top: 530px; }

  .service-info {
    position: absolute;
    top: 26px;
    right: 34px;
    font-weight: 700;
    font-size: 17px;
    line-height: 1.1;
    text-align: left;
  }
  .tagline {
    position: absolute;
    top: 118px;
    left: 0;
    width: 100%;
    text-align: center;
    font-size: 34px;
  }
  .tagline-letter {
    color: var(--brand-pink);
    font-size: 48px;
  }
  .rep-fields {
    position: absolute;
    bottom: 26px;
    left: 0;
    width: 100%;
    text-align: center;
    font-weight: 700;
    font-size: 17px;
    line-height: 1.2;
  }

  .logo {
    position: absolute;
    right: 60px;
    top: 130px;
    display: flex;
    align-items: center;
    gap: 16px;
  }
  .logo-dot {
    width: 22px;
    height: 22px;
    border-radius: 50%;
    background: var(--brand-pink);
  }
  .logo-name {
    font-size: 84px;
    font-weight: 400;
    color: var(--brand-grey);
    letter-spacing: 2px;
    line-height: 1;
  }
  .front-website {
    position: absolute;
    right: 64px;
    top: 226px;
    font-size: 16px;
    font-weight: 700;
    color: var(--brand-pink);
  }
</style>
</head>
<body>
  <main class="canvas">
    <section class="card card-back" aria-label="Card back with contact details">
      <div class="service-info">
        <p>Customer Service : 1 800 482</p>
        <p>Website : www.gokelvara.example</p>
      </div>
      <p class="tagline">Kelvra is all about <span class="tagline-letter">K</span></p>
      <div class="rep-fields">
        <p>Name</p>
        <p>Phone</p>
        <p>Mail id</p>
      </div>
    </section>

    <section class="card card-front" aria-label="Card front with brand name">
      <div class="logo">
        <span class="logo-dot"></span>
        <span class="logo-name">Kelvra</span>
      </div>
      <p class="front-website">www.gokelvara.example</p>
    </section>
  </main>
</body>
</html>
```